IT Network Consultancy - Business Card

t4 linkways is a IT network consultancy based in London. We're looking for a smart, modern and professional business card design. Our website is here: www.t4linkways.co.uk

Key things that should be included on the card (with examples):

Company Logo
Name
Position / Job Title: Network Consultant
Mobile Phone Number: +44 (0) 7700 900418
Land Line: +44 (0) 1632 960274
Email Address: name@t4linkways.co.uk
Web Site URL: www.t4linkways.co.uk

Target Market(s)

Large enterprise / global companies / corporates

Industry/Entity Type

Business

Requirements
Must have
• Incorporate our logo - which is attached to the project. They are in AI format (can be opened in Inkscape).

The design should be double sided and fit on a UK standard 85mm × 55mm card and be in a format that retains the quality when printed.
Nice to have
• The project does not have to conform to the colour of our website but this should give you inspiration of the style we like.
Should not have
• Bright colours. Pictures are not necessary.

```html
<!DOCTYPE html>
<html lang="en">
<head>
<meta charset="utf-8">
<title>t4 linkways – Business Card</title>
<link href="https://fonts.googleapis.com/css2?family=Jost:wght@300;400;500;600&display=swap" rel="stylesheet">
<style>
  :root {
    --page: #ffffff;
    --slate-dark: #44525d;
    --slate-mid: #53626d;
    --slate-light: #5f6e79;
    --band: #f1f3f4;
    --band-edge: #e2e6e8;
    --ink: #3d4953;
    --ink-soft: #7d8890;
    --brand-light: #e4e8ea;
    --brand: #5a6770;
  }
  * { margin: 0; padding: 0; box-sizing: border-box; }
  html, body {
    width: 1200px; height: 900px; overflow: hidden;
    background: var(--page);
    font-family: "Jost", "Futura", sans-serif;
  }
  .canvas { position: relative; width: 1200px; height: 900px; }
  .card {
    position: absolute; top: 296px;
    width: 500px; height: 313px;
    box-shadow: 2px 3px 5px rgba(0,0,0,0.3);
    overflow: hidden;
    background: linear-gradient(160deg, var(--slate-light), var(--slate-dark));
  }
  .card--front { left: 84px; }
  .card--back { left: 619px; }
  .band {
    position: absolute; left: 0; right: 0;
    background: linear-gradient(90deg, var(--band-edge), var(--band) 50%, var(--band-edge));
  }
  .card--front .band { top: 121px; height: 158px; }
  .card--back .band { top: 120px; height: 72px; }
  .wordmark {
    position: absolute;
    font-weight: 300; color: var(--brand);
    text-transform: uppercase; letter-spacing: 0.06em;
    white-space: nowrap; line-height: 1;
    display: flex; align-items: center; gap: 10px;
  }
  .wordmark__dot { display: inline-block; border-radius: 50%; }
  .card--front .wordmark { left: 33px; top: 76px; font-size: 30px; color: var(--brand-light); }
  .card--front .wordmark__dot { width: 22px; height: 22px; background: #c9cfd3; }
  .card--back .wordmark { left: 0; right: 0; top: 138px; justify-content: center; font-size: 38px; }
  .card--back .wordmark__dot { width: 28px; height: 28px; background: #9aa3a9; }
  .holder { position: absolute; right: 35px; top: 136px; text-align: right; }
  .holder__name { font-size: 18px; font-weight: 600; color: var(--ink); line-height: 1.1; }
  .holder__role { font-size: 13px; font-weight: 400; color: var(--ink-soft); margin-top: 2px; }
  .contact {
    position: absolute; left: 40px; top: 192px;
    list-style: none; font-size: 14px; color: var(--ink); line-height: 18px;
  }
  .contact__label { font-weight: 600; display: inline-block; width: 20px; }
</style>
</head>
<body>
<main class="canvas">

  <section class="card card--front" aria-label="Business card front">
    <div class="band"></div>
    <div class="wordmark"><span class="wordmark__dot"></span>T4 Linkways</div>
    <div class="holder">
      <p class="holder__name">Daniel Hartley</p>
      <p class="holder__role">Network Consultant</p>
    </div>
    <ul class="contact">
      <li><span class="contact__label">p.</span>+44 (0) 1632 960274</li>
      <li><span class="contact__label">m.</span>+44 (0) 7700 900418</li>
      <li><span class="contact__label">e.</span>danielhartley@t4linkways.co.uk</li>
      <li><span class="contact__label">w.</span>www.t4linkways.co.uk</li>
    </ul>
  </section>

  <section class="card card--back" aria-label="Business card back">
    <div class="band"></div>
    <div class="wordmark"><span class="wordmark__dot"></span>T4 Linkways</div>
  </section>

</main>
</body>
</html>
```